Fleet Service Tri Fold Flyer

I am looking to come up with a flyer design to hand out showing our services. I will upload more info with working, but in the mean time want to just have a flyer to pass out. I have uploaded our logo and the images for it. I also uploaded what our trucks look like for ideas, as well as a business card.

Industry/Entity Type

Mobile Hydraulics and Fleet Service

Colors
0054AA
0677BA
7BADD7
CADEEF
E8F1F8
F0912C
F2A743
F7CA91
FBE8D2
FDF5EE

Requirements
Must have
• I uploaded a PDF with wording for the flyer

```html
<!DOCTYPE html>
<html lang="en">
<head>
<meta charset="utf-8">
<title>Keystone Fleet Service – Tri-Fold Flyer</title>
<link rel="stylesheet" href="https://fonts.googleapis.com/css2?family=Open+Sans:wght@300;400;700;800&family=Archivo+Black&display=swap">
<style>
  :root {
    --navy: #143e6c;
    --navy-deep: #0f335c;
    --orange: #f2a743;
    --orange-deep: #e3972c;
    --orange-soft: #f7ca91;
    --white: #ffffff;
    --ink: #1b1b1b;
    --heading-blue: #1a4274;
  }
  * { box-sizing: border-box; margin: 0; padding: 0; }
  html, body { width: 1200px; height: 887px; overflow: hidden; background: #ececec; }
  .flyer { position: relative; width: 1200px; height: 887px; font-family: "Open Sans", sans-serif; }
  .flyer-art { position: absolute; inset: 0; }

  .panel-heading {
    position: absolute; left: 56px; top: 78px;
    font-weight: 800; font-size: 33px; line-height: 34px;
    color: var(--heading-blue); letter-spacing: 0.3px;
  }
  .panel-body {
    position: absolute; left: 55px; top: 200px; width: 284px;
    font-size: 12.6px; line-height: 18.6px; color: var(--ink);
    text-align: justify;
  }
  .panel-body p + p { margin-top: 18.6px; }

  .rule { position: absolute; left: 527px; width: 146px; height: 6px; background: var(--orange); }
  .rule-top { top: 54px; }
  .rule-bottom { top: 180px; }
  .mission {
    position: absolute; left: 420px; top: 90px; width: 360px;
    text-align: center; color: var(--white);
    font-weight: 400; font-size: 17px; line-height: 24px; text-transform: uppercase;
  }
  .badge-text {
    position: absolute; left: 551px; top: 262px; width: 108px;
    text-align: center; color: var(--navy); font-weight: 800; font-style: normal;
    font-size: 26px; line-height: 26px;
  }
  .badge-text small { display: block; font-size: 15px; line-height: 18px; }

  .contact-title {
    position: absolute; left: 436px; top: 386px;
    color: var(--white); font-weight: 700; font-size: 29px; line-height: 34px;
  }
  .contact-name {
    position: absolute; left: 436px; top: 424px;
    color: var(--white); font-weight: 700; font-size: 23px; line-height: 28px;
  }
  .contact-phone {
    position: absolute; left: 479px; top: 503px;
    color: var(--white); font-weight: 700; font-size: 42px; line-height: 52px;
  }
  .contact-lines {
    position: absolute; left: 481px;
    color: var(--white); font-weight: 700; font-size: 16.5px; line-height: 24px;
  }
  .contact-web { top: 564px; }
  .contact-address { top: 622px; left: 479px; }

  .cover-title {
    position: absolute; left: 838px; top: 58px;
    font-family: "Archivo Black", sans-serif; font-size: 37px; line-height: 41px;
    color: var(--white); text-shadow: 2px 2px 0 #0a2340;
  }
  .brand-name {
    position: absolute; left: 940px; top: 770px; width: 240px;
    text-align: center; color: var(--white);
    font-weight: 800; font-size: 28px; line-height: 32px; letter-spacing: 1px;
  }
</style>
</head>
<body>
<main class="flyer">
  <svg class="flyer-art" width="1200" height="887" viewBox="0 0 1200 887" aria-hidden="false">
    <defs>
      <linearGradient id="orangeFill" x1="0" y1="0" x2="0" y2="1">
        <stop offset="0" stop-color="#f6b64f"/>
        <stop offset="1" stop-color="#dc9527"/>
      </linearGradient>
      <linearGradient id="workshopTones" x1="0" y1="0" x2="1" y2="1">
        <stop offset="0" stop-color="#5d6670"/>
        <stop offset="0.5" stop-color="#8b8f94"/>
        <stop offset="1" stop-color="#3d3f44"/>
      </linearGradient>
      <linearGradient id="mechanicTones" x1="0" y1="0" x2="1" y2="1">
        <stop offset="0" stop-color="#4f5a66"/>
        <stop offset="0.55" stop-color="#9a9ea3"/>
        <stop offset="0.8" stop-color="#b8444f"/>
        <stop offset="1" stop-color="#d8ad3a"/>
      </linearGradient>
    </defs>

    <rect class="base-navy" width="1200" height="887" fill="var(--navy)"/>

    <!-- left panel white field -->
    <path class="left-field" d="M0,0 H262 C310,70 350,120 400,152 L400,735 C300,670 150,560 0,449 Z" fill="var(--white)"/>
    <path class="left-sweep" d="M278,0 C320,70 360,125 400,160" fill="none" stroke="var(--orange-soft)" stroke-width="9"/>
    <path class="left-sweep-thin" d="M305,0 C345,65 375,110 400,135" fill="none" stroke="var(--orange)" stroke-width="3"/>

    <!-- middle panel orange band -->
    <path class="middle-band" d="M400,170 C520,255 660,292 800,298 L800,752 C650,745 520,712 400,678 Z" fill="url(#orangeFill)"/>
    <path class="middle-band-edge" d="M400,162 C520,248 660,285 800,290" fill="none" stroke="var(--orange-soft)" stroke-width="5"/>

    <!-- right panel sweeps -->
    <path class="right-sweep" d="M800,290 C950,286 1100,235 1200,160" fill="none" stroke="var(--orange-soft)" stroke-width="8"/>
    <path class="right-sweep-deep" d="M800,300 C950,296 1100,248 1200,175" fill="none" stroke="var(--orange)" stroke-width="6"/>
    <path class="cover-photo" role="img" aria-label="Photo: mechanic in red shirt and cap servicing a truck brake disc in a workshop"
          d="M800,306 C950,302 1100,256 1200,182 L1200,585 C1100,648 950,700 800,712 Z" fill="url(#mechanicTones)"/>
    <path class="right-low-sweep" d="M800,716 C950,705 1100,655 1200,590" fill="none" stroke="var(--orange)" stroke-width="5"/>

    <!-- long bottom line -->
    <path class="bottom-line" d="M330,790 C520,822 700,805 1200,640" fill="none" stroke="var(--orange)" stroke-width="3"/>
    <path class="left-arc" d="M0,618 C30,640 45,650 60,660" fill="none" stroke="var(--orange)" stroke-width="4"/>

    <!-- left circle photo -->
    <circle class="photo-ring" cx="198" cy="655" r="154" fill="var(--orange)"/>
    <circle class="workshop-photo" role="img" aria-label="Photo: technician repairing a heavy truck wheel hub with brake chambers and tools on the floor"
            cx="198" cy="655" r="142" fill="url(#workshopTones)"/>

    <!-- 24/7 badge -->
    <circle class="badge" cx="605" cy="288" r="54" fill="var(--white)"/>

    <!-- contact icons -->
    <g class="icon icon-phone" fill="none" stroke="var(--white)" stroke-width="2.4">
      <circle cx="452" cy="530" r="15"/>
      <path d="M446,522 l4,-1 l2,5 l-3,2 c1,3 3,5 6,6 l2,-3 l5,2 l-1,4 c-9,0 -15,-6 -15,-15 z" fill="var(--white)" stroke="none"/>
    </g>
    <g class="icon icon-web" fill="none" stroke="var(--white)" stroke-width="2.2">
      <circle cx="452" cy="588" r="15"/>
      <circle cx="452" cy="588" r="9"/>
      <ellipse cx="452" cy="588" rx="4" ry="9"/>
      <line x1="443" y1="588" x2="461" y2="588"/>
    </g>
    <g class="icon icon-pin" fill="none" stroke="var(--white)" stroke-width="2.2">
      <circle cx="450" cy="646" r="15"/>
      <path d="M450,656 c-5,-6 -7,-9 -7,-12 a7,7 0 0 1 14,0 c0,3 -2,6 -7,12 z"/>
      <circle cx="450" cy="644" r="2.2" fill="var(--white)"/>
    </g>
  </svg>

  <h2 class="panel-heading">EMERGENCY<br>ROADSIDE<br>ASSISTANCE</h2>
  <div class="panel-body">
    <p>Between our different locations we have several fully equipped &amp; stocked service trucks to meet your needs on the road. We offer onsite roadside repair &amp; diagnostics. Whether it’s during regular operating hours, after hours, weekends, or Holidays.</p>
    <p>We understand that your business depends on your truck being on the road and meeting your promised delivery schedule. Whether it's at your shop, jobsite, or on the road, we are there to serve. We carry many of the common parts and items needed on the roadside.</p>
  </div>

  <div class="rule rule-top"></div>
  <p class="mission">Keystone Fleet Service<br>strives to be your go to call<br>for on-location</p>
  <div class="rule rule-bottom"></div>
  <div class="badge-text">24/7<small>SERVICE</small></div>

  <p class="contact-title">CONTACT US NOW!!</p>
  <p class="contact-name">DANA WHITLOCK</p>
  <p class="contact-phone">555 014 2290</p>
  <p class="contact-lines contact-web">www.keystonefleet.example<br>dana@keystonefleet.example</p>
  <p class="contact-lines contact-address">4120 Harbor Mill Road,<br>Cedar Falls FL 34000</p>

  <h1 class="cover-title">KEYSTONE<br>MOBILE<br>HYDRAULIC<br>REPAIR</h1>
  <p class="brand-name">KEYSTONE FLEET</p>
</main>
</body>
</html>
```